Amber Tides: Lantern Tales from Seven Winters by the Northern Sea and Other Small Wonders

Good day! I am excited to work again with you, amazing designers! This time I am looking for the cover design of my book.
Dimensions 6” x 9”
The book name is as my name project. I love simplicity, but yet that is impactful. I love colours, I don't have a specific colour in mind, but I like the mustard colour as the one in the logo of my company. I am open to ideas! I have attached some cover samples that I like so that it gives a better idea of what I have on mind.
I am looking for something that looks professional, yet, not super serious, that it's approachable to people. Something that calls their attention at first glance.
I am working with my editor and my interior designer as well to finalize this part of the book. I will be working with the person that I select for the book design to finalize it.
About the book, here a passage of an unedited version of the introduction for guidance :
My intention is to take you on a journey to help you to understand what is going on in your mind so that you get out from anything that is holding you back in your life. My intention is to guide you to start fully living and experiencing a life that your mind even have yet conceived. To experience a life where you live fearless and without suffering. Living your life where you are the navigator and the creator of how you are experiencing it and you are living in a world of possibilities where there are no limitations.
For it, we will start to understand more about the mind and about the brain. I am not a neuroscientist and neither I consider my self an expert in the workings of the brain, what I know is the result of my fascination about our brain. This curiosity and the part of me that likes to understand how things work took me to read, research and learn about how our brain works and how its intrinsic mechanisms are subconsciously influencing and limiting us. I encourage you to stay on this part, it can be a bit technical, but understanding how it works will empower you not to allow your mind to dictate the way you approach your life and to live on autopilot.
We will continue to describe how you have been programmed throughout your life, putting you inside a box limited by your subconscious beliefs and ideas about the world. In this part, we will also discuss what ego is, how it is subconsciously limiting you and how the ways of when ego manifests itself are limiting you and making you suffer. Now that you know how you have been enclosed in your mind for all your life, we will move to discuss how you can get out of it. You will learn how to master your emotions to eliminate your suffering and not allow them to control the direction of your life and use them as a mechanism to get out from your programed mind. We continue to discuss how to leverage the power of your mind and harness your power of choice. Finally, I invite you to see yourself as a holistic being so that you start truly living and take control over the direction of your life, by nourishing and taking care of all those aspects of you utilizing their wisdom and synergy to achieve higher connection within yourself, your soul and live your life in a higher level of consciousness with peace, flow, love and purpose.

```html
<!DOCTYPE html>
<html lang="en">
<head>
<meta charset="utf-8">
<title>Amber Tides — Book Cover</title>
<link rel="stylesheet" href="https://fonts.googleapis.com/css2?family=Lilita+One&family=Rubik+Mono+One&family=Montserrat:wght@600;700&display=swap">
<style>
  :root {
    --mustard: #fcaa1f;
    --mustard-light: #fdc25a;
    --mustard-deep: #f29a12;
    --ink-navy: #2a1aa3;
    --paper-white: #ffffff;
    --shadow-navy: #1b1270;
  }
  html, body {
    margin: 0;
    padding: 0;
    width: 849px;
    height: 1200px;
    overflow: hidden;
    background: var(--mustard);
  }
  .cover {
    position: relative;
    width: 849px;
    height: 1200px;
    background: var(--mustard);
    overflow: hidden;
  }
  .cover-illustration {
    position: absolute;
    left: 175px;
    top: 20px;
    width: 450px;
    height: 290px;
    border-radius: 40px;
    background: radial-gradient(ellipse at 40% 45%, var(--mustard-light) 0%, var(--mustard) 75%);
  }
  .title {
    position: absolute;
    left: 0;
    right: 0;
    top: 420px;
    margin: 0;
    text-align: center;
    font-weight: normal;
  }
  .title-lead {
    display: block;
    font-family: "Lilita One", sans-serif;
    font-size: 112px;
    line-height: 1;
    letter-spacing: 2px;
    color: var(--ink-navy);
    white-space: nowrap;
  }
  .title-line {
    display: block;
    font-family: "Rubik Mono One", sans-serif;
    color: var(--paper-white);
    white-space: nowrap;
    line-height: 1.1;
  }
  .title-line--first { font-size: 54px; margin-top: 14px; }
  .title-line--second { font-size: 38px; margin-top: 6px; }
  .title-raised {
    display: inline-block;
    transform: translateY(-10px) rotate(-4deg);
    text-shadow: 3px 3px 0 var(--shadow-navy), 6px 6px 0 var(--shadow-navy);
  }
  .subtitle {
    position: absolute;
    left: 0;
    right: 0;
    top: 740px;
    margin: 0;
    text-align: center;
    font-family: "Montserrat", sans-serif;
    font-weight: 700;
    font-size: 21px;
    line-height: 1.45;
    letter-spacing: 1.5px;
    color: var(--ink-navy);
  }
  .dots {
    position: absolute;
    left: 0;
    right: 0;
    top: 842px;
    display: flex;
    justify-content: center;
    gap: 14px;
  }
  .dots span {
    width: 20px;
    height: 20px;
    border-radius: 50%;
    background: var(--ink-navy);
  }
  .author {
    position: absolute;
    left: 0;
    right: 0;
    top: 1012px;
    margin: 0;
    text-align: center;
    font-family: "Lilita One", sans-serif;
    font-size: 46px;
    line-height: 1.05;
    letter-spacing: 3px;
    color: var(--ink-navy);
  }
</style>
</head>
<body>
  <main class="cover">
    <div class="cover-illustration" role="img" aria-label="Cartoon illustration of a large brain beside a small person, linked by a trail of dots like a thought bubble"></div>

    <h1 class="title">
      <span class="title-lead">AMBER TIDES:</span>
      <span class="title-line title-line--first">LANTERN TALES</span>
      <span class="title-line title-line--second"><span class="title-raised">FROM</span> SEVEN WINTERS</span>
    </h1>

    <p class="subtitle">BY THE NORTHERN SEA<br>AND OTHER SMALL WONDERS</p>

    <div class="dots" aria-hidden="true"><span></span><span></span><span></span></div>

    <p class="author">MARISOL<br>VENTURA</p>
  </main>
</body>
</html>
```